Brightfernrx website

We are a weight loss clinic and we need a website built. please look at these websites for content and style. Just need like 5 pages see samples. AI files of logo are not avail yet so use sample for place set

https://glowshiftstudio.com/
ortanvital.com
https://pinecrestclinicalbodybalance.com/
https://yourslimmingnook.com/
https://qrvskinstudio.com/treatments/weight-loss-injections/

Target Market(s)

Women

Industry/Entity Type

weight loss

Coding

Coded - Design and coding required

Number of Pages Required

5+ page

Requirements
Nice to have
• please make look like a medspa website

```html
<!DOCTYPE html>
<html lang="en">
<head>
<meta charset="utf-8">
<title>Brightfernrx – Weight Loss, Wellness &amp; Rejuvenation</title>
<link href="https://fonts.googleapis.com/css2?family=EB+Garamond:ital,wght@0,400;0,500;0,600;1,400&family=Arimo:ital,wght@0,400;0,700;1,400&display=swap" rel="stylesheet">
<style>
:root{
  --blue:#1f8dcc;
  --green:#77a642;
  --ink:#1f1f1f;
  --body:#333;
  --grey-band:#f1f1f1;
  --light:#f6f6f6;
  --white:#fff;
}
*{margin:0;padding:0;box-sizing:border-box}
html,body{width:1200px;height:4101px;overflow:hidden}
body{position:relative;background:var(--white);font-family:"Arimo",Arial,sans-serif;color:var(--body)}
.abs{position:absolute}
.serif{font-family:"EB Garamond",Georgia,serif}
.photo{position:absolute}

/* header */
.logo{position:absolute;display:flex;align-items:center;gap:8px;font-family:"EB Garamond",Georgia,serif;font-weight:600;color:var(--blue);letter-spacing:.5px;white-space:nowrap}
.logo-dot{width:26px;height:26px;border-radius:50%;background:var(--blue)}
.tagline{position:absolute;left:168px;top:41px;font-family:"EB Garamond",Georgia,serif;font-size:6.5px;letter-spacing:.6px;color:#777;white-space:nowrap}
.nav a{position:absolute;top:27px;white-space:nowrap;font-family:"EB Garamond",Georgia,serif;font-weight:600;font-size:11px;color:var(--ink);text-decoration:none;letter-spacing:.3px}
.nav a.active{color:var(--blue)}
.book-btn{position:absolute;left:936px;top:19px;width:130px;height:34px;border:2px solid var(--blue);border-radius:17px;display:flex;align-items:center;gap:10px;padding-left:4px;font-family:"EB Garamond",Georgia,serif;font-weight:600;font-size:13px;color:var(--blue);letter-spacing:.5px}
.book-btn i{width:24px;height:24px;border-radius:50%;background:var(--blue)}

/* shared type */
.eyebrow{position:absolute;font-family:"EB Garamond",Georgia,serif;font-weight:500;font-size:17px;letter-spacing:.4px;text-transform:uppercase;white-space:nowrap}
.eyebrow.green{color:var(--green)}
.eyebrow.blue{color:var(--blue)}
.heading{position:absolute;font-family:"EB Garamond",Georgia,serif;font-weight:500;color:var(--ink);font-size:30px;line-height:32px;white-space:nowrap}
.copy{position:absolute;font-size:11px;line-height:22px;color:var(--body)}
.btn{position:absolute;height:33px;border-radius:17px;background:var(--blue);display:flex;align-items:center;gap:10px;padding:0 14px 0 4px;font-family:"EB Garamond",Georgia,serif;font-weight:500;font-size:14px;letter-spacing:.6px;color:var(--white);white-space:nowrap}
.btn i{width:25px;height:25px;border-radius:50%;background:var(--white)}

/* hero */
.hero{position:absolute;left:0;top:0;width:1200px;height:640px;background:linear-gradient(180deg,#f4f4f4 0%,#efefef 100%)}
.hero-photo{left:573px;top:0;width:627px;height:600px;background:radial-gradient(ellipse at 62% 55%,#a9cf7f 0%,#cfe3b5 35%,rgba(239,239,239,0) 70%)}
.hero-photo::after{content:"";position:absolute;left:120px;top:40px;width:270px;height:520px;border-radius:140px 140px 40px 40px;background:linear-gradient(180deg,#d9b59d,#c79a80);opacity:.55}
.dots{position:absolute;left:580px;top:584px;display:flex;gap:5px;align-items:center}
.dots span{width:5px;height:5px;border-radius:50%;background:#9fbcd4}
.dots span.on{width:9px;height:9px;background:var(--blue)}

/* about */
.brand-emblem{left:111px;top:655px;width:470px;height:440px;border-radius:50%;background:radial-gradient(circle at 50% 50%,#f5f5f5 0%,#eeeeee 60%,#fff 72%)}

/* band 2 */
.band-grey{position:absolute;left:0;top:1130px;width:1200px;height:434px;background:var(--grey-band)}
.frame{position:absolute;left:552px;top:1106px;width:410px;height:522px;background:var(--white);padding:6px;box-shadow:0 2px 8px rgba(0,0,0,.08)}
.frame .photo{position:relative;width:100%;height:100%;background:linear-gradient(160deg,#e7e2dd 0%,#d8c8bb 45%,#c9b3a3 70%,#e9e9ea 100%)}
.leaf-deco{left:900px;top:1140px;width:280px;height:300px;border-radius:50%;background:radial-gradient(circle,#dfeccf 0%,rgba(241,241,241,0) 70%)}

/* services */
.service{position:absolute;top:1848px;width:274px;text-align:center}
.service .disc{width:274px;height:274px;border-radius:50%;position:relative;overflow:hidden}
.service h3{margin-top:18px;font-family:"EB Garamond",Georgia,serif;font-weight:600;font-size:15.5px;letter-spacing:.6px;color:var(--ink)}
.service.mid h3{color:var(--green)}
.disc.weight{background:linear-gradient(150deg,#c9b8aa 0%,#7f8f8e 50%,#5d7378 100%)}
.disc.wellness{background:radial-gradient(circle at 50% 40%,#3e9b8a 0%,#1f6f73 70%);border:4px solid #163e5c}
.disc.rejuv{background:linear-gradient(150deg,#e8e6e4 0%,#d6c2b0 55%,#eeeeee 100%)}
.disc p{position:absolute;left:38px;right:38px;top:75px;font-family:"EB Garamond",Georgia,serif;font-size:11.5px;line-height:20px;color:var(--white)}

/* cta */
.cta{position:absolute;left:0;top:2231px;width:1200px;height:315px;background:linear-gradient(90deg,#79a845 0%,#5f9d6e 45%,#3c8fa0 75%,#2f89a8 100%)}
.cta .heading{color:var(--white);width:1200px;text-align:center;left:0;top:92px}
.cta .copy{color:var(--white);left:212px;width:776px;top:132px;text-align:center}
.cta .eyebrow{color:var(--white)}

/* testimonial */
.stars{position:absolute;left:534px;top:2624px}
.arrow{position:absolute;top:2696px}
.quote-mark{position:absolute;font-family:"EB Garamond",Georgia,serif;font-weight:700;font-size:80px;line-height:1;color:var(--green)}
.quote{position:absolute;left:218px;top:2664px;width:764px;text-align:center;font-style:italic;font-size:12px;line-height:22px;color:var(--body)}
.quote .gap{display:inline-block;width:84px}
.signature{position:absolute;left:0;width:1200px;top:2812px;text-align:center;font-family:"EB Garamond",Georgia,serif;font-style:italic;font-size:24px;color:var(--green)}

/* gallery */
.gallery-bg{position:absolute;left:0;top:2905px;width:1200px;height:780px;background:var(--light)}
.pair{position:absolute;width:276px;height:156px;background:var(--white);padding:4px;display:flex;gap:4px;box-shadow:0 1px 4px rgba(0,0,0,.08)}
.pair div{flex:1}
.pair.feature{outline:3px solid #d9d9d9}

/* footer */
.footer{position:absolute;left:0;top:3630px;width:1200px;height:471px}
.foot-col{position:absolute;top:3808px}
.foot-col h4{font-family:"EB Garamond",Georgia,serif;font-weight:500;font-size:16px;letter-spacing:.5px;color:var(--white);margin-bottom:8px}
.foot-col li{list-style:none;display:flex;align-items:center;gap:10px;font-family:"EB Garamond",Georgia,serif;font-size:12.5px;line-height:22px;color:var(--white)}
.foot-col li b{display:inline-block;width:6px;height:6px;border-radius:50%;background:var(--white)}
.foot-col .info li{align-items:flex-start;line-height:21px;margin-bottom:8px}
.foot-col .info li svg{margin-top:5px;flex:none}
.foot-rule{position:absolute;left:56px;top:4006px;width:1090px;height:1px;background:rgba(255,255,255,.55)}
.copyright{position:absolute;left:0;width:1200px;top:4031px;text-align:center;font-family:"EB Garamond",Georgia,serif;font-size:12px;color:var(--white)}
</style>
</head>
<body>

<!-- HERO -->
<section class="hero" aria-label="Welcome">
  <div class="photo hero-photo" role="img" aria-label="Smiling woman with bare shoulders against a soft green glow"></div>
  <svg class="abs" style="left:0;top:0" width="1200" height="640" viewBox="0 0 1200 640" aria-hidden="true">
    <path d="M0 570 C90 600 150 635 230 630 C320 625 330 545 420 535 C520 525 560 580 640 585 C760 590 820 515 920 505 C1020 495 1080 560 1200 560 L1200 640 L0 640 Z" fill="#ffffff"/>
  </svg>
</section>

<header>
  <div class="logo" style="left:134px;top:12px;font-size:23px">
    <span class="logo-dot"></span>BRIGHTFERNRX
  </div>
  <div class="tagline">WEIGHT LOSS | WELLNESS | REJUVENATION</div>
  <nav class="nav">
    <a class="active" style="left:422px" href="#">HOME</a>
    <a style="left:481px" href="#">SERVICES</a>
    <a style="left:552px" href="#">WHY CHOOSE US</a>
    <a style="left:667px" href="#">SPECIALS</a>
    <a style="left:740px" href="#">TESTIMONIALS</a>
    <a style="left:843px" href="#">CONTACT US</a>
  </nav>
  <div class="book-btn"><i></i>BOOK NOW</div>
</header>

<div class="eyebrow green" style="left:134px;top:177px">Welcome to Brightfernrx</div>
<h1 class="heading" style="left:133px;top:202px;font-size:30px;line-height:35px">Lorem ipsum dolor sit amet, con<br>sectetur adipiscing elit, sed do<br>eiusmod tempor incidi.</h1>
<p class="copy" style="left:134px;top:310px;width:450px;line-height:21px">Lorem ipsum dolor sit amet, consectetur adipiscing elit, sed do eiusmod tempor incididunt ut labore et dolore magna aliqua.</p>
<div class="btn" style="left:134px;top:365px"><i></i>GET STARTED</div>
<div class="dots"><span class="on"></span><span></span><span></span><span></span></div>

<!-- ABOUT -->
<section aria-label="About">
  <div class="photo brand-emblem" role="img" aria-label="Large brand emblem decoration"></div>
  <div class="eyebrow blue" style="left:693px;top:670px">About Brightfernrx</div>
  <h2 class="heading" style="left:648px;top:703px">Lorem ipsum dolor sit ametcon<br>sectetur adipiscing elit.</h2>
  <p class="copy" style="left:648px;top:775px;width:436px">Lorem ipsum dolor sit amet, consectetur adipiscing elit, sed do eiusmod temp or incididunt ut labore et dolore magna aliqua. unde omnis iste natus error sit voluptatem accusantium doloremque laudantium, totam rem aperiam, eaque ipsa quae ab illo inventore veritatis et quasi architecto beatae vitae dicta sunt explicabo. Nemo enim ipsam voluptatem quia voluptas sit aspernatur aut odit aut fugit, sed quia consequuntur magni dolores eos qui ratione voluptatem sequi nesciunt. Neque porro quisquam est, qui dolorem ipsum quia dolor sit amet, consectetur, adipisci velit, sed quia non numquam eius modi tempora incidunt ut labore et dolore magnam aliquam quaerat voluptatem.</p>
  <div class="btn" style="left:648px;top:981px"><i></i>LEARN MORE</div>
</section>

<!-- ENCOURAGING -->
<section aria-label="Encouraging you every step of the way">
  <div class="band-grey"></div>
  <div class="photo leaf-deco" role="img" aria-label="Soft green leaf decoration"></div>
  <div class="frame"><div class="photo" role="img" aria-label="Woman in a white crop top and shorts measuring her waist with a tape"></div></div>
  <div class="eyebrow blue" style="left:97px;top:1188px">Lorem ipsum dolor</div>
  <h2 class="heading" style="left:57px;top:1221px">Encouraging you every step of<br>the way.</h2>
  <p class="copy" style="left:57px;top:1292px;width:436px">Lorem ipsum dolor sit amet, consectetur adipiscing elit, sed do eiusmod temp or incididunt ut labore et dolore magna aliqua. unde omnis iste natus error sit voluptatem accusantium doloremque laudantium, totam rem aperiam, eaque ipsa quae ab illo inventore veritatis et quasi architecto beatae vitae dicta sunt explicabo. Nemo enim ipsam voluptatem quia voluptas sit aspernatur aut odit aut fugit, sed quia consequuntur magni dolores eos qui ratione voluptatem sequi nesciunt Neque porro quisquam est.</p>
  <div class="btn" style="left:57px;top:1455px"><i></i>LEARN MORE</div>
</section>

<!-- WHY CHOOSE US -->
<section aria-label="Why choose us">
  <div class="eyebrow green" style="left:176px;top:1680px">Why choose us</div>
  <h2 class="heading" style="left:164px;top:1712px">Lorem ipsum dolor sit amet consectetur eiusmod<br>adipiscing elit.</h2>
  <p class="copy" style="left:164px;top:1784px;width:880px;line-height:21px">Lorem ipsum dolor sit amet, consectetur adipiscing elit, sed do eiusmod tempor incididunt ut labore et dolore magna aliqua. Ut enim ad minim veniam, quis nostrud exercitation ullamco laboris nisi ut aliquip ex ea commodo consequat.</p>

  <div class="service" style="left:165px">
    <div class="disc weight" role="img" aria-label="Tattooed waist wrapped in a measuring tape"></div>
    <h3>WEIGHT LOSS</h3>
  </div>
  <div class="service mid" style="left:465px">
    <div class="disc wellness" role="img" aria-label="Green forest with water, wellness scene">
      <p>Lorem ipsum dolor sit amet, consectetur adipiscing elit, sed do eiusmod tempor incididunt ut labore et dolore magna aliqua. Quis ipsum suspendisse ultrices gravida. Risus commodo viverra maecenas accumsan lacus vel facilisis.</p>
    </div>
    <h3>WELLNESS</h3>
  </div>
  <div class="service" style="left:762px">
    <div class="disc rejuv" role="img" aria-label="Woman receiving a facial treatment with a brush"></div>
    <h3>REJUVENATION</h3>
  </div>
</section>

<!-- CTA -->
<section class="cta" aria-label="Get started today">
  <div class="eyebrow" style="left:538px;top:58px">Get started today</div>
  <h2 class="heading">Reaching your weight loss goal is definitely doable!</h2>
  <p class="copy">Lorem ipsum dolor sit amet, consectetur adipiscing elit, sed do eiusmod tempor incididunt ut labore et dolore magna aliqua. unde omnis iste natus error sit voluptatem accusantium doloremque laudantium, totam rem aperiam, eaque ipsa quae ab illo inventore veritatis et quasi architecto beatae vitae dicta sunt explicabo. Nemo enim ipsam voluptatem quia voluptas sit aspernatur aut odit aut .</p>
  <div class="btn" style="left:528px;top:220px"><i></i>LEARN MORE</div>
</section>

<!-- TESTIMONIAL -->
<section aria-label="Testimonials">
  <div class="stars" aria-label="Five stars">
    <svg width="160" height="22" viewBox="0 0 160 22" aria-hidden="true">
      <g fill="var(--blue)">
        <polygon points="11,0 14,7.5 22,8 16,13 18,21 11,16.5 4,21 6,13 0,8 8,7.5"/>
        <polygon transform="translate(27 0)" points="11,0 14,7.5 22,8 16,13 18,21 11,16.5 4,21 6,13 0,8 8,7.5"/>
        <polygon transform="translate(54 0)" points="11,0 14,7.5 22,8 16,13 18,21 11,16.5 4,21 6,13 0,8 8,7.5"/>
        <polygon transform="translate(81 0)" points="11,0 14,7.5 22,8 16,13 18,21 11,16.5 4,21 6,13 0,8 8,7.5"/>
        <polygon transform="translate(108 0)" points="11,0 14,7.5 22,8 16,13 18,21 11,16.5 4,21 6,13 0,8 8,7.5"/>
      </g>
    </svg>
  </div>
  <svg class="arrow" style="left:150px" width="20" height="38" viewBox="0 0 20 38" aria-label="Previous"><polyline points="18,1 2,19 18,37" fill="none" stroke="#222" stroke-width="1.5"/></svg>
  <svg class="arrow" style="left:1030px" width="20" height="38" viewBox="0 0 20 38" aria-label="Next"><polyline points="2,1 18,19 2,37" fill="none" stroke="#222" stroke-width="1.5"/></svg>
  <div class="quote-mark" style="left:250px;top:2648px">&#8220;</div>
  <div class="quote-mark" style="left:740px;top:2780px">&#8221;</div>
  <p class="quote"><span class="gap"></span>Lorem ipsum dolor sit amet, consectetur adipiscing elit, sed do eiusmod tempor incididunt ut labore et dolore magna aliqua. Ut enim ad minim veniam, quis nostrud exercitation ullamco laboris nisi ut aliquip ex ea commodo consequat. Duis aute irure dolor in reprehenderit in voluptate velit esse cillum dolore eu fugiat nulla pariatur. Excepteur sint occaecat cupidatat non proident, sunt in culpa qui officia deserunt mollit anim id est laborum.incididunt ut labore et dolore magna aliqua. Ut enim ad minim veniam, quis nostrud exercitation ullamco laboris nisi ut aliquip ex ea commodo consequat. Duis aute irure dolor in reprehenderit in voluptate velit esse cillum dolore eu fugiat nulla pariatur.</p>
  <div class="signature">Marisol Verene</div>
</section>

<!-- GALLERY -->
<section aria-label="Customers gallery">
  <div class="gallery-bg"></div>
  <div class="eyebrow blue" style="left:560px;top:2960px">Before after</div>
  <h2 class="heading" style="left:0;width:1200px;text-align:center;top:2994px">Our Customers Gallery</h2>
  <p class="copy" style="left:164px;top:3034px;width:872px;text-align:center;line-height:21px">Lorem ipsum dolor sit amet, consectetur adipiscing elit, sed do eiusmod tempor incididunt ut labore et dolore magna aliqua. Ut enim ad minim veniam, quis nostrud exercitation ullamco laboris nisi ut aliquip ex ea commodo consequat.</p>

  <div class="pair" style="left:175px;top:3095px" role="img" aria-label="Before and after body results in blue swimwear"><div style="background:linear-gradient(160deg,#d7b59b,#3fa2c2)"></div><div style="background:linear-gradient(160deg,#e2c6ad,#38b4cf)"></div></div>
  <div class="pair feature" style="left:462px;top:3095px" role="img" aria-label="Before and after jawline contouring"><div style="background:linear-gradient(160deg,#c9c9c9,#8d8d8d)"></div><div style="background:linear-gradient(160deg,#cfcfcf,#8a8a8a)"></div></div>
  <div class="pair" style="left:748px;top:3095px" role="img" aria-label="Before and after selfie results in green sportswear"><div style="background:linear-gradient(160deg,#e9e9e9,#7ea35c)"></div><div style="background:linear-gradient(160deg,#eeeeee,#8fb062)"></div></div>

  <div class="pair" style="left:175px;top:3259px" role="img" aria-label="Before and after facial skin treatment"><div style="background:linear-gradient(160deg,#e8d2c2,#c8a48c)"></div><div style="background:linear-gradient(160deg,#efe0d4,#d9bfae)"></div></div>
  <div class="pair" style="left:462px;top:3259px" role="img" aria-label="Before and after mirror body results"><div style="background:linear-gradient(160deg,#6c6358,#c09e86)"></div><div style="background:linear-gradient(160deg,#6f665c,#b78f77)"></div></div>
  <div class="pair" style="left:748px;top:3259px" role="img" aria-label="Before and after cheek skin close-up"><div style="background:linear-gradient(160deg,#e6c5b0,#c99478)"></div><div style="background:linear-gradient(160deg,#f0d2be,#d8a487)"></div></div>

  <div class="pair" style="left:175px;top:3425px" role="img" aria-label="Before and after beach results in coral swimwear"><div style="background:linear-gradient(160deg,#8fb7cc,#e07159)"></div><div style="background:linear-gradient(160deg,#9cc0d2,#ea7662)"></div></div>
  <div class="pair" style="left:462px;top:3425px" role="img" aria-label="Before and after eye area wrinkle treatment"><div style="background:linear-gradient(160deg,#f1f1f1,#c9b0a2)"></div><div style="background:linear-gradient(160deg,#f3f3f3,#c6ab9b)"></div></div>
  <div class="pair" style="left:748px;top:3425px" role="img" aria-label="Before and after body results in black lingerie"><div style="background:linear-gradient(160deg,#c8d3e4,#2a2a33)"></div><div style="background:linear-gradient(160deg,#cfd9e8,#2e2e38)"></div></div>
</section>

<!-- FOOTER -->
<footer>
  <div class="photo" style="left:0;top:3600px;width:1200px;height:160px;background:linear-gradient(180deg,rgba(246,246,246,0) 0%,#f1eed6 60%,#ece6c2 100%)" role="img" aria-label="Yellow measuring tape draped along the wave"></div>
  <svg class="footer" viewBox="0 0 1200 471" aria-hidden="true">
    <path d="M0 20 C100 40 170 110 260 125 C350 140 430 90 520 100 C620 112 680 165 780 150 C880 135 960 80 1060 75 C1120 72 1170 85 1200 95 L1200 471 L0 471 Z" fill="var(--green)"/>
  </svg>

  <div class="logo" style="left:162px;top:3850px;font-size:26px;color:var(--white)">
    <span class="logo-dot" style="background:var(--white)"></span>BRIGHTFERNRX
  </div>

  <div class="foot-col" style="left:455px">
    <h4>QUICK LINKS</h4>
    <ul>
      <li><b></b>Home</li>
      <li><b></b>Services</li>
      <li><b></b>Why Choose Us</li>
      <li><b></b>Specials</li>
      <li><b></b>Testimonials</li>
      <li><b></b>Contact Us</li>
    </ul>
  </div>
  <div class="foot-col" style="left:636px">
    <h4>FOLLOW US</h4>
    <ul>
      <li><b></b>Circlefeed</li>
      <li><b></b>Photoloop</li>
      <li><b></b>Chirpline</li>
      <li><b></b>Workweb</li>
      <li><b></b>Vidstream</li>
    </ul>
  </div>
  <div class="foot-col" style="left:803px">
    <h4>HEAD OFFICE INFO</h4>
    <ul class="info">
      <li><svg width="10" height="13" viewBox="0 0 10 13"><path d="M5 0a5 5 0 0 1 5 5c0 3.5-5 8-5 8S0 8.5 0 5a5 5 0 0 1 5-5z" fill="#fff"/><circle cx="5" cy="5" r="1.8" fill="var(--green)"/></svg><span>123, Lorem ipsum dolor sit amet,<br>consectetur adipiscing elit.</span></li>
      <li><svg width="11" height="11" viewBox="0 0 11 11"><rect width="11" height="11" rx="2" fill="#fff"/><path d="M3 2.5l1.5 1.5-1 1a5 5 0 0 0 2.5 2.5l1-1L8.5 8 7.5 9A6 6 0 0 1 2 3.5z" fill="var(--green)"/></svg><span>+1 555 014 2290</span></li>
      <li><svg width="12" height="9" viewBox="0 0 12 9"><rect width="12" height="9" rx="1" fill="#fff"/><polyline points="0.5,0.5 6,5 11.5,0.5" fill="none" stroke="var(--green)"/></svg><span>hello@brightfernrx.example</span></li>
    </ul>
  </div>

  <div class="foot-rule"></div>
  <p class="copyright">© copyrights 2022 BRIGHTFERNRX &nbsp;&nbsp;|&nbsp;&nbsp;&nbsp; All rights reserved.</p>
</footer>

</body>
</html>
```